Business card and Stationery for data intelligence company

We need a new design for our business cards and stationery (Business Letter templates and a Quote example on Word, but it MUST work on Google Doc as well).

We are a software company based in Ireland and UK. Our product is "Quarla", data intelligence platform with beautiful visualizations, graph capabilities (things are interconnected), powerful, flexible, it can manage Big Data and Streaming information. It's modern and relatively open source.
Our company will provide data intelligence for law enforcements, pharmaceuticals, and similar high end customers.

We'll launch a new website soon. At the moment it's http://www.quarla.tech if you want to take a look. This is our youtube channel in case you need it to understand what Quarla is: https://www.youtube.com/c/quarlatechchannel

We changed the logo so please use the logo I attach here.

We'd like the output to be cool and modern but elegant and "business" at the same time. It should inspire simple sophistication, "unity" "intent" "purpose" yet subtly very advanced and innovative.

The name "Quarla" does NOT refer to sirens (mithological creatures) as well as the warning devices. It means Quantum Unified Archival Record Layer Array. Please use our logo's colors and if you want to something like the "graph" image.

```html
<!DOCTYPE html>
<html lang="en">
<head>
<meta charset="utf-8">
<title>Quarla Business Card</title>
<link rel="stylesheet" href="https://fonts.googleapis.com/css2?family=Montserrat:wght@400;500&family=Roboto:wght@400;500&display=swap">
<style>
  :root {
    --backdrop: #3b3b3d;
    --card: #2f2f31;
    --card-edge: #2a2a2c;
    --accent: #f4ac33;
    --silver: #b5b5b5;
    --text: #f2f2f2;
  }
  * { margin: 0; padding: 0; box-sizing: border-box; }
  html, body {
    width: 1200px; height: 900px; overflow: hidden;
    background: var(--backdrop);
    font-family: "Roboto", Arial, sans-serif;
  }
  .stage { position: relative; width: 1200px; height: 900px; }
  .card {
    position: absolute;
    width: 620px; height: 360px;
    background: var(--card);
    border-radius: 20px;
    box-shadow: 0 18px 40px rgba(0,0,0,0.45);
    overflow: hidden;
  }
  .card--back { left: 500px; top: 80px; }
  .card--front { left: 80px; top: 450px; }

  .brand { display: flex; align-items: center; gap: 14px; }
  .brand__dot { border-radius: 50%; background: var(--accent); flex: none; }
  .brand__name {
    font-family: "Montserrat", Arial, sans-serif;
    font-weight: 500;
    color: var(--accent);
    letter-spacing: 0.16em;
    line-height: 1;
  }
  .brand__tagline {
    font-family: "Montserrat", Arial, sans-serif;
    font-weight: 400;
    color: var(--silver);
    letter-spacing: 0.38em;
    text-transform: uppercase;
  }

  .card--back .brand-block {
    position: absolute; left: 50%; top: 50%;
    transform: translate(-50%, -50%);
  }
  .card--back .brand__dot { width: 52px; height: 52px; }
  .card--back .brand__name { font-size: 56px; }
  .card--back .brand__tagline { font-size: 15px; margin: 6px 0 0 66px; }

  .card--front .brand-block { position: absolute; left: 44px; top: 38px; }
  .card--front .brand__dot { width: 40px; height: 40px; }
  .card--front .brand__name { font-size: 42px; }
  .card--front .brand__tagline { font-size: 11px; margin: 4px 0 0 54px; }

  .contact { position: absolute; left: 44px; top: 150px; color: var(--text); }
  .contact__name { font-size: 22px; font-weight: 500; }
  .contact__role { font-size: 14px; color: var(--accent); margin-top: 2px; }
  .contact__address { font-size: 15px; line-height: 1.4; margin-top: 10px; }
  .contact__list { list-style: none; margin-top: 10px; }
  .contact__item { display: flex; align-items: center; gap: 10px; font-size: 15px; line-height: 1.65; }
  .contact__icon { width: 18px; height: 18px; flex: none; }
</style>
</head>
<body>
<main class="stage">
  <section class="card card--back" aria-label="Card back">
    <div class="brand-block">
      <div class="brand">
        <span class="brand__dot"></span>
        <span class="brand__name">QUARLA</span>
      </div>
      <div class="brand__tagline">Data Intelligence</div>
    </div>
  </section>

  <section class="card card--front" aria-label="Card front">
    <div class="brand-block">
      <div class="brand">
        <span class="brand__dot"></span>
        <span class="brand__name">QUARLA</span>
      </div>
      <div class="brand__tagline">Data Intelligence</div>
    </div>

    <div class="contact">
      <p class="contact__name">Ronan Keaveny</p>
      <p class="contact__role">Managing Director</p>
      <p class="contact__address">Harbourline House 58 Merrion Quay<br>Dublin D02 K7X4</p>
      <ul class="contact__list">
        <li class="contact__item">
          <svg class="contact__icon" viewBox="0 0 18 18" aria-hidden="true">
            <circle cx="9" cy="9" r="9" fill="var(--accent)"/>
            <path d="M6 4.5c.6 0 1.3 1.6 1.3 2.1S6.5 7.4 6.6 7.9c.3 1.3 2.2 3.2 3.5 3.5.5.1.8-.7 1.3-.7s2.1.7 2.1 1.3-1 1.6-1.8 1.5C8.6 13.2 4.8 9.4 4.5 6.3 4.4 5.5 5.4 4.5 6 4.5z" fill="var(--card)"/>
          </svg>
          07845 209 316
        </li>
        <li class="contact__item">
          <svg class="contact__icon" viewBox="0 0 18 18" aria-hidden="true">
            <circle cx="9" cy="9" r="9" fill="var(--accent)"/>
            <rect x="4.3" y="5.8" width="9.4" height="6.4" rx="0.8" fill="none" stroke="var(--card)" stroke-width="1.2"/>
            <path d="M4.6 6.2 9 9.6l4.4-3.4" fill="none" stroke="var(--card)" stroke-width="1.2"/>
          </svg>
          name@quarla.tech
        </li>
        <li class="contact__item">
          <svg class="contact__icon" viewBox="0 0 18 18" aria-hidden="true">
            <circle cx="9" cy="9" r="9" fill="var(--accent)"/>
            <g fill="none" stroke="var(--card)" stroke-width="1.1">
              <circle cx="9" cy="9" r="5"/>
              <ellipse cx="9" cy="9" rx="2.2" ry="5"/>
              <path d="M4 9h10M5 6.5h8M5 11.5h8"/>
            </g>
          </svg>
          www.quarla.tech
        </li>
      </ul>
    </div>
  </section>
</main>
</body>
</html>
```